We are a small NZ based company looking to rebrand our eco chem free cleaning product Purova

This product was launched in 2021. The brand and labeling were aimed at the consumer who cared that the cleaning products they bought into their home were not only effective but non-harmful to their families and the environment. The label was a little bohemian/ natural. We feel that the labels now need to be more chic and classy, They need to look stylish in a country cottage as well as a high end minimalist home. Colours need to be mute so as to fit with most decors.
We need help with font colour and type - layout and balance. Trigger/ pump colour.
I have attached photos of our current range and labels
A couple of mock ups we are working on - (struggling with )
A colour pallet
The two last PNG files are closer to where we want to end up but they are not really right.

The products are sold online only
Our website is www.purova.co.nz
The Brand board that we had done sometime ago is that last file.
Most of the colours on the labels are ok - except the apricot on the foaming hand soap bottle and the colour on the all purpose bottle - neither of which we love.
The Fair Tide bottles are closer to what we are thinking.
Canva Links
https://www.sketchloft.example/design/QWRTplmzx41/hbnKyeTgrQuvs93LdwPoZa/edit
https://www.sketchloft.example/design/QWRTvbn7UoXc/kPmWq2RzTyhNb4VfGsLeXd/edit
https://www.sketchloft.example/design/QWRTzh3KLaNp/yt6BemRwPoiLx81CvdNqTe/edit
https://www.sketchloft.example/design/QWRTfk8MsaTq/Lu5DrpXwgYoBj72MnhKzsc/edit

Target Market(s)

Mothers who care about the products they bring into there homes but also want the product to look good in the home

Industry/Entity Type

Cleaning products

Requirements
Must have
• Design must be chic - and be able to sit and look great in any modern bathroom or kitchen.

```html
<!DOCTYPE html>
<html lang="en">
<head>
<meta charset="utf-8">
<title>Purova label range</title>
<link rel="stylesheet" href="https://fonts.googleapis.com/css2?family=Montserrat:wght@400;500;700&family=Marcellus&display=swap">
<style>
  :root {
    --canvas: #ffffff;
    --teal: #6f979c;
    --rose: #c09a9a;
    --panel: #ffffff;
    --ink: #3a3a3a;
    --bloom-line: rgba(255,255,255,0.18);
  }
  * { box-sizing: border-box; margin: 0; padding: 0; }
  html, body { width: 1200px; height: 800px; overflow: hidden; background: var(--canvas); }
  body { position: relative; font-family: "Montserrat", Arial, sans-serif; color: var(--ink); }

  .label {
    position: absolute;
    top: 268px;
    width: 540px;
    height: 264px;
    overflow: hidden;
  }
  .label--laundry { left: 40px; --accent: var(--teal); }
  .label--cleaner { left: 620px; --accent: var(--rose); }

  .label__floral {
    position: absolute;
    inset: 0;
    background:
      radial-gradient(circle at 22% 30%, var(--bloom-line), transparent 45%),
      radial-gradient(circle at 80% 70%, var(--bloom-line), transparent 45%),
      var(--accent);
  }

  .label__panel {
    position: absolute;
    left: 50%;
    top: 10px;
    bottom: 0;
    width: 220px;
    transform: translateX(-50%);
    background: var(--panel);
    border-radius: 110px 110px 0 0;
    padding: 48px 16px 12px;
    display: flex;
    flex-direction: column;
    align-items: center;
    text-align: center;
  }

  .brand { display: flex; flex-direction: column; align-items: center; }
  .brand__name {
    font-size: 22px;
    font-weight: 500;
    color: var(--ink);
    line-height: 1;
    letter-spacing: 4px;
    text-transform: uppercase;
  }
  .brand__tagline { font-size: 7px; font-weight: 500; color: var(--ink); letter-spacing: 0.6px; margin-top: 6px; }

  .product-name {
    font-family: "Marcellus", Georgia, serif;
    font-weight: 400;
    color: var(--accent);
    font-size: 27px;
    line-height: 0.95;
    margin-top: 12px;
  }
  .product-desc { font-size: 8px; line-height: 1.25; margin-top: 5px; text-align: left; width: 100%; }
  .dots { margin-top: 6px; width: 120px; border-top: 3px dotted var(--accent); }
  .uses { margin-top: 8px; width: 100%; text-align: left; font-size: 9.5px; line-height: 1.35; }
  .uses span { border-bottom: 1px solid var(--ink); }
  .volume { margin-top: auto; align-self: flex-end; font-size: 12px; font-weight: 700; color: var(--accent); }
</style>
</head>
<body>

  <section class="label label--laundry">
    <div class="label__floral" role="img" aria-label="Fine white line drawing of chamomile flowers and stems across a muted teal ground"></div>
    <div class="label__panel">
      <div class="brand">
        <span class="brand__name">Purova</span>
        <span class="brand__tagline">THE POWER OF CHAMOMILE</span>
      </div>
      <h2 class="product-name">laundry liquid</h2>
      <p class="product-desc">effective clean,harsh on dirt and gentle on your clothes</p>
      <div class="dots"></div>
      <p class="uses"><span>machine | handwash | soaker</span><br>stain remover | hot or cold water</p>
      <p class="volume">1L</p>
    </div>
  </section>

  <section class="label label--cleaner">
    <div class="label__floral" role="img" aria-label="Fine white line drawing of chamomile flowers and stems across a dusty rose ground"></div>
    <div class="label__panel">
      <div class="brand">
        <span class="brand__name">Purova</span>
        <span class="brand__tagline">THE POWER OF CHAMOMILE</span>
      </div>
      <h2 class="product-name">all purpose<br>cleaner</h2>
      <p class="product-desc">everyday cleaning including benchtops, high chairs, dishes &amp; so much more!</p>
      <div class="dots"></div>
      <p class="uses"><span>surfaces | stains | grease &amp; grime</span><br>great for everyday cleaning</p>
      <p class="volume">500ml</p>
    </div>
  </section>

</body>
</html>
```